Pelin Thai Massage Double Sided Flyer Luxury

I require a double sided flyer
we are a Thai Massage Spa
Would like gold, deep purple and bronze colours
Something eye catching and looks professional

```html
<!DOCTYPE html>
<html lang="en">
<head>
<meta charset="utf-8">
<title>Pelin Thai Massage – Double Sided Flyer</title>
<link href="https://fonts.googleapis.com/css2?family=Montserrat:wght@700&family=Open+Sans:wght@400;600;700&display=swap" rel="stylesheet">
<style>
  :root {
    --canvas: #eff2f3;
    --purple: #48084f;
    --gold: #f9c532;
    --gold-text: #f6c23c;
    --bronze: #a8680e;
    --photo-warm-a: #f3c27a;
    --photo-warm-b: #d9774a;
    --photo-cream-a: #f1e7cf;
    --photo-cream-b: #c99a5c;
    --photo-towel-a: #8d8a86;
    --photo-towel-b: #c94f76;
  }
  * { margin: 0; padding: 0; box-sizing: border-box; }
  html, body { width: 1200px; height: 1200px; overflow: hidden; background: var(--canvas); }
  .canvas { position: relative; width: 1200px; height: 1200px; }
  .page {
    position: absolute; top: 327px; width: 386px; height: 546px;
    background: var(--purple); overflow: hidden;
    font-family: "Open Sans", Arial, sans-serif; color: var(--gold-text);
  }
  .page--front { left: 196px; }
  .page--back { left: 618px; }
  .page__art { position: absolute; inset: 0; width: 386px; height: 546px; }
  .brand { position: absolute; top: 12px; left: 300px; width: 80px; text-align: center; }
  .brand__mark { width: 26px; height: 26px; border-radius: 50%; background: var(--gold); margin: 0 auto 6px; }
  .brand__name { font-size: 6.6px; font-weight: 400; white-space: nowrap; }
  .heading { position: absolute; left: 0; right: 0; text-align: center; font-family: "Montserrat", Arial, sans-serif; font-weight: 700; }
  .welcome__title { top: 322px; font-size: 15.5px; }
  .welcome__body { position: absolute; top: 350px; left: 0; right: 0; text-align: center; font-size: 6.4px; line-height: 9.5px; }
  .menu__title { top: 280px; font-size: 15.7px; letter-spacing: 0.3px; }
  .menu__intro { position: absolute; top: 302px; left: 0; right: 0; text-align: center; font-size: 6.3px; line-height: 9px; }
  .menu__rule { position: absolute; top: 333px; left: 64px; width: 258px; height: 1px; background: var(--bronze); }
  .menu__list { position: absolute; top: 345px; left: 22px; right: 10px; }
  .menu__section { font-family: "Montserrat", Arial, sans-serif; font-weight: 700; font-size: 16px; line-height: 16.5px; }
  .menu__sub { font-family: "Montserrat", Arial, sans-serif; font-weight: 700; font-size: 11.7px; line-height: 14px; }
  .menu__price { font-family: "Montserrat", Arial, sans-serif; font-weight: 700; font-size: 11.5px; line-height: 14px; }
  .menu__desc { font-size: 6.3px; line-height: 9px; }
  .gap-lg { margin-top: 10px; }
  .gap-md { margin-top: 10px; }
  .footer { position: absolute; top: 518px; left: 0; right: 0; text-align: center; font-size: 6.4px; font-weight: 700; line-height: 9.5px; }
  .footer a { color: inherit; text-decoration: underline; }
</style>
</head>
<body>
<div class="canvas">

  <!-- Front side -->
  <section class="page page--front">
    <svg class="page__art" viewBox="0 0 386 546">
      <defs>
        <linearGradient id="warmPhoto" x1="0" y1="0" x2="1" y2="1">
          <stop offset="0" stop-color="var(--photo-warm-a)"/>
          <stop offset="1" stop-color="var(--photo-warm-b)"/>
        </linearGradient>
        <linearGradient id="towelPhoto" x1="0" y1="0" x2="1" y2="0">
          <stop offset="0" stop-color="var(--photo-towel-a)"/>
          <stop offset="0.6" stop-color="var(--photo-towel-b)"/>
          <stop offset="1" stop-color="var(--photo-towel-a)"/>
        </linearGradient>
      </defs>
      <!-- top swoosh bands, stacked under the photo -->
      <path d="M0,0 L160,0 Q310,26 386,110 L386,246 Q193,362 0,274 Z" fill="var(--bronze)"/>
      <path d="M0,0 L160,0 Q310,26 386,110 L386,240 Q193,356 0,268 Z" fill="var(--gold)"/>
      <path d="M0,0 L190,0 Q325,36 386,140 L386,228 Q193,344 0,256 Z" fill="var(--bronze)"/>
      <path d="M0,0 L200,0 Q330,40 386,150 L386,214 Q193,330 0,242 Z"
            fill="url(#warmPhoto)" role="img" aria-label="Photo of a woman relaxing during a back massage"/>
      <!-- bottom swoosh bands and photo -->
      <path d="M0,486 Q190,339 386,465 L386,546 L0,546 Z" fill="var(--bronze)"/>
      <path d="M0,492 Q190,345 386,471 L386,546 L0,546 Z" fill="var(--gold)"/>
      <path d="M0,502 Q190,355 386,481 L386,546 L0,546 Z"
            fill="url(#towelPhoto)" role="img" aria-label="Photo of rolled towels decorated with pink flowers"/>
    </svg>
    <div class="brand">
      <div class="brand__mark"></div>
      <div class="brand__name">Pelin Thai Massage</div>
    </div>
    <h1 class="heading welcome__title">Welcome to Luxury</h1>
    <p class="welcome__body">
      Set in the heart of Elmfield,<br>
      Pelin Thai Massage will allow you to immerse yourself in a place<br>
      where your wellbeing and rejuvenation is at the centre of what we do.<br>
      UsingThai traditions, our highly trained therapists offer revitalising<br>
      body treatments with their deep tissue massage techniques.<br>
      In their hands, you will see and feel immediate results.
    </p>
  </section>

  <!-- Back side -->
  <section class="page page--back">
    <svg class="page__art" viewBox="0 0 386 546">
      <defs>
        <linearGradient id="creamPhoto" x1="0" y1="0" x2="1" y2="1">
          <stop offset="0" stop-color="var(--photo-cream-a)"/>
          <stop offset="1" stop-color="var(--photo-cream-b)"/>
        </linearGradient>
      </defs>
      <!-- lower swoosh bands, stacked under the photo -->
      <path d="M0,0 L386,0 L386,272 C190,290 70,244 0,150 Z" fill="var(--bronze)"/>
      <path d="M0,0 L386,0 L386,264 C190,284 70,236 0,142 Z" fill="var(--gold)"/>
      <path d="M0,0 L386,0 L386,250 C184,270 66,220 0,112 Z" fill="var(--bronze)"/>
      <path d="M0,0 L290,0 Q356,26 386,78 L386,240 C180,262 60,210 0,102 Z"
            fill="url(#creamPhoto)" role="img" aria-label="Photo of a woman receiving a face massage beside a candle and flowers"/>
      <!-- top-right corner swoosh -->
      <path d="M282,0 Q352,22 386,68 L386,78 Q356,26 290,0 Z" fill="var(--bronze)"/>
      <path d="M282,0 L386,0 L386,68 Q352,22 282,0 Z" fill="var(--gold)"/>
    </svg>
    <h2 class="heading menu__title">MASSAGES</h2>
    <p class="menu__intro">
      Restore balance. Revive your senses. Discover all the ways Pelin Thai Massage<br>
      Can breathe new life into your body and soul.
    </p>
    <div class="menu__rule"></div>
    <div class="menu__list">
      <div class="menu__section">MASSAGES<br>DEEP TISSUE MASSAGE</div>
      <div class="menu__price gap-lg">60 minutes £45</div>
      <div class="menu__desc">Oil massage personalised, light to firm pressure</div>
      <div class="menu__price gap-md">90 minutes £55</div>
      <div class="menu__desc">Oil massage, medium to firm pressure</div>
      <div class="menu__sub gap-md">THAI FLOOR TRADTIONAL MASSAGE</div>
      <div class="menu__price">60 minutes £45</div>
      <div class="menu__desc">Dry massage, medium to firm pressure applying stretching technique</div>
    </div>
    <p class="footer">
      Pelin Thai Massage | 14 Mill Row | Harrowgate | HG4 2TL | 0142 3870256 | <a>www.pelinthaispa.co.uk</a><br>
      Gift Vouchers Available
    </p>
  </section>

</div>
</body>
</html>
```